Heavy Equipment Rental Company Looking for Attractive Sign Design

We need a new sign for our forklift rental company in Southern California called Ridgeline Lift Partners. We also sell, service and move forklifts and other equipment, but forklift rentals are our main business. Our old sign on the street is deteriorating quickly. I've attached a photo of the old sign - it is approximately 52" high and 48" wide, but may be made 6" or so taller if needed. The old sign is included more to reference the information than the design - the old design definitely has issues (no SketchHive at the time). The smaller sign reading Borvex dealer is not needed. We want the sign to be simple, clean and easy to read, but of course also attractive and professional. We would like the same information on it as is on the previous sign, but it may be re-arranged. The number 2200 is the street number. Here are the essential elements:
2200 (street number)
Ridgeline Lift Partners (business name)
714-382-0476 (phone)
www.ridgelinelifts-example.com (website)
Forklift Rentals and Sales (main businesses)
If possible, we would like the names of our 2 primary brands:
Borvex and Tavilo Forklifts
Although, if there's no way to implement them nicely, then we can leave them off.

Target Market(s)

Industrial, Construction

Industry/Entity Type

Construction

Colors
0355a3

Requirements
Must have
• Bold, clean, easy to read, with the necessary information.
Nice to have
• Our main machines are all painted blue, so some blue in the design would be nice. In our industry, Borvex forklifts and Tavilo forklifts are two different brands but have good reputations. It would be nice if we can include them in the design, although a nice design is more important than including the brand names.
Should not have
• Small or difficult to read text. Colors or fonts that are too playful.

```html
<!DOCTYPE html>
<html lang="en">
<head>
<meta charset="utf-8">
<title>Ridgeline Lift Partners Sign</title>
<link href="https://fonts.googleapis.com/css2?family=Noto+Sans:wght@400;700&family=Roboto+Condensed:wght@700&display=swap" rel="stylesheet">
<style>
:root{
  --brand-blue:#0355a3;
  --deep-blue:#0b3f72;
  --ink-blue:#1f3d93;
  --white:#ffffff;
  --skyline:#dfe8f3;
}
*{margin:0;padding:0;box-sizing:border-box}
html,body{width:1200px;height:1200px;overflow:hidden;background:var(--white)}
.sign{position:relative;width:1200px;height:1200px;background:var(--white);font-family:"Noto Sans",sans-serif;overflow:hidden}
.sweep{position:absolute;left:0;top:0;width:1200px;height:1200px}
.street-number{position:absolute;left:383px;top:41px;width:250px;height:119px;background:var(--brand-blue);border-radius:10px;color:var(--white);font-family:"Roboto Condensed",sans-serif;font-weight:700;font-size:94px;letter-spacing:-6px;line-height:119px;text-align:center}
.business-name{position:absolute;left:0;top:238px;width:1010px;text-align:center;color:var(--brand-blue);font-size:104px;line-height:128px;font-weight:400}
.offer-lead{position:absolute;left:94px;top:560px;color:var(--deep-blue);font-size:62px;font-weight:400}
.offer-main{position:absolute;right:40px;top:662px;color:var(--white);font-size:56px;font-weight:400}
.phone{position:absolute;right:28px;top:770px;color:var(--white);font-size:106px;font-weight:400;letter-spacing:0}
.web-band{position:absolute;left:0;top:916px;width:1200px;height:68px;background:var(--brand-blue);color:var(--white);font-size:40px;line-height:68px;text-align:center;letter-spacing:5px}
.web-band strong{font-weight:700}
.skyline-area{position:absolute;left:0;top:984px;width:1200px;height:216px;background:linear-gradient(to bottom,var(--white) 0%,var(--skyline) 45%,var(--skyline) 100%)}
.brand{position:absolute;top:1052px;font-size:74px;line-height:90px;font-weight:700;letter-spacing:10px}
.brand-borvex{left:124px;color:var(--brand-blue)}
.brand-tavilo{left:694px;color:var(--ink-blue)}
</style>
</head>
<body>
<div class="sign">
  <svg class="sweep" viewBox="0 0 1200 1200" aria-hidden="true">
    <defs>
      <linearGradient id="sweepFade" x1="0" y1="0" x2="0" y2="1">
        <stop offset="0" stop-color="#ffffff"/>
        <stop offset="0.35" stop-color="#6f8fb0"/>
        <stop offset="0.6" stop-color="#1d5283"/>
        <stop offset="1" stop-color="#083f72"/>
      </linearGradient>
    </defs>
    <path d="M0 916 C 500 820, 1000 520, 1200 40 L1200 916 Z" fill="url(#sweepFade)"/>
  </svg>

  <div class="street-number">2200</div>
  <h1 class="business-name">Ridgeline Lift<br>Partners</h1>
  <p class="offer-lead">Rentals and Sales of</p>
  <p class="offer-main">High Reach Forklifts</p>
  <p class="phone">714-382-0476</p>
  <p class="web-band">www.<strong>ridgelinelifts-example</strong>.com</p>

  <div class="skyline-area" role="img" aria-label="Faint pale blue city skyline silhouette behind the brand names"></div>
  <div class="brand brand-borvex">BORVEX</div>
  <div class="brand brand-tavilo">TAVILO</div>
</div>
</body>
</html>
```